New Crowdfunding site Fundlark needs banner ads

I’m looking for 4 standard size banner ads for www.fundlark.example to be used by TradeQuill Affiliates in order to bring new crowdfunding projects to the platform.
728x90
160x600
300x250
180x160

Succesful designers will put on our Mentors list so that the project owner can also get their specific project banners from our designers. Designers can also become our affiliates either to promote Fundlark.example or individual projects.
Updates

Please note updated brief

Thank you to those that have submitted designs so far.
Please be reminded that the invitation will close tomorrow after which we will make our choice

Thanks for input so far.
Please note project closes tomorrow (Sunday) after which we will choose.

Target Market(s)

Target is a project owner with a project requiring $10,000 or more in any field including business and/or non-profits. Any country.
Inventors, creatives, communities, hardware or software, consumer items,

Industry/Entity Type

Crowdfunding

Font styles to use
Sans Serif

Requirements
Must have
• Clear button call to action based on our USPs shown on the home page but especially the use of Affiliate Networks to promote their project to the widest possible audience.

Text and button text should be editable (see png preference).
Call to action could be based on "Free Crowdfunding Consultation - is your project viable" or "Get Your Free Guide to Succesful Crowdfunding"
Nice to have
• .png format preferred with separate objects.
Some animation preferred in the button.

```html
<!DOCTYPE html>
<html lang="en">
<head>
<meta charset="utf-8">
<title>Fundlark banner ads</title>
<link rel="stylesheet" href="https://fonts.googleapis.com/css2?family=Michroma&family=Orbitron:wght@500&family=Cabin:wght@500;600&family=Roboto+Condensed:ital,wght@1,700&display=swap">
<style>
  :root {
    --stage-light: #e4e4e4;
    --stage-dark: #2a2a2a;
    --blue-deep: #0a4f9e;
    --blue-mid: #1187d6;
    --blue-bright: #27b4ee;
    --white: #ffffff;
    --paper: #f2f2f2;
    --ink-blue: #1537e0;
    --free-blue: #1b2fe6;
    --funding-green: #1fb21f;
  }
  * { box-sizing: border-box; margin: 0; padding: 0; }
  html, body { width: 1200px; height: 900px; overflow: hidden; }
  body {
    position: relative;
    background: radial-gradient(ellipse 75% 60% at 35% 45%, var(--stage-light) 0%, #b8b8b8 45%, #6a6a6a 75%, var(--stage-dark) 100%);
    font-family: "Cabin", sans-serif;
  }
  .banner {
    position: absolute;
    overflow: hidden;
    background: var(--paper);
    box-shadow: 0 3px 8px rgba(0,0,0,0.45);
  }
  .backdrop {
    position: absolute;
    background: radial-gradient(ellipse at 50% 100%, var(--blue-bright) 0%, var(--blue-mid) 55%, var(--blue-deep) 100%);
  }
  .curve { position: absolute; left: 0; width: 100%; }
  .brand-mark {
    position: absolute;
    display: flex; flex-direction: column; align-items: center; justify-content: center; gap: 6px;
    color: var(--white);
    font-family: "Cabin", sans-serif; font-weight: 600;
  }
  .brand-mark .dot { width: 34px; height: 34px; border-radius: 50%; background: var(--white); opacity: .9; }
  .equation { font-family: "Orbitron", sans-serif; font-weight: 500; color: var(--white); white-space: nowrap; }
  .equation .funding { color: var(--funding-green); }
  .offer {
    font-family: "Michroma", sans-serif;
    color: var(--white);
    text-shadow: 0 1px 2px rgba(0,0,0,.4);
    text-align: center;
    white-space: nowrap;
  }
  .cta { position: absolute; }
  .cta text { font-family: "Roboto Condensed", sans-serif; font-style: italic; font-weight: 700; fill: var(--white); }

  /* Skyscraper */
  .sky { left: 894px; top: 66px; width: 120px; height: 600px; }
  .sky .logo-zone { position: absolute; left: 0; top: 0; width: 120px; height: 124px;
    background: linear-gradient(180deg, var(--blue-mid), #0f78c8); border-bottom: 1px solid #7fd3ff; }
  .sky .brand-mark { inset: 0; font-size: 18px; }
  .sky .backdrop { left: 0; top: 124px; width: 120px; height: 260px; }
  .sky .curve { top: 340px; height: 50px; }
  .sky .headline { position: absolute; left: 0; top: 135px; width: 120px; color: var(--white); text-align: center;
    font-family: "Cabin", sans-serif; font-weight: 600; text-shadow: 0 1px 2px rgba(0,0,0,.4); white-space: nowrap; }
  .sky .headline .big { display: block; font-size: 27px; line-height: 24px; }
  .sky .headline .free { color: var(--free-blue); text-shadow: none; }
  .sky .headline .small { display: block; font-size: 19.5px; line-height: 24px; font-weight: 500; }
  .sky .headline .first-small { margin-top: 2px; }
  .sky .equation { position: absolute; left: 0; top: 390px; width: 120px; text-align: center; color: var(--ink-blue); }
  .sky .equation .word { display: block; font-size: 19px; line-height: 20px; }
  .sky .equation .op { display: block; font-size: 11px; line-height: 19px; }
  .sky .equation .funding { display: block; font-size: 22px; line-height: 22px; }
  .sky .cta { left: 17px; top: 512px; }

  /* Medium rectangle */
  .rect { left: 555px; top: 416px; width: 300px; height: 250px; }
  .rect .header { position: absolute; left: 0; top: 0; width: 300px; height: 50px;
    background: linear-gradient(180deg, #1790da, #0c6dbf); border-bottom: 1px solid #8ad8ff;
    display: flex; align-items: center; padding-left: 12px; font-size: 18px; }
  .rect .header .funding { font-size: 21px; margin-left: 6px; }
  .rect .backdrop { left: 0; top: 50px; width: 300px; height: 200px; }
  .rect .curve { top: 150px; height: 100px; }
  .rect .brand-mark { left: 8px; top: 66px; width: 108px; height: 104px; font-size: 17px; }
  .rect .offer { position: absolute; left: 110px; top: 67px; width: 190px; font-size: 15px; line-height: 29px; letter-spacing: 2px; }
  .rect .cta { left: 151px; top: 193px; }

  /* Leaderboard */
  .leader { left: 286px; top: 716px; width: 728px; height: 90px; }
  .leader .backdrop { left: 135px; top: 0; width: 593px; height: 90px; }
  .leader .side { position: absolute; left: 0; top: 0; width: 135px; height: 90px;
    background: linear-gradient(180deg, #1585d2, var(--blue-deep)); border-right: 1px solid #5ab8ec; }
  .leader .brand-mark { inset: 0; font-size: 17px; gap: 4px; }
  .leader .brand-mark .dot { width: 26px; height: 26px; }
  .leader .curve { left: auto; right: 0; top: 0; width: 80px; height: 90px; }
  .leader .offer { position: absolute; left: 139px; top: 3px; width: 440px; font-size: 15px; line-height: 28px; letter-spacing: 3.5px; }
  .leader .equation { position: absolute; left: 139px; top: 62px; width: 440px; text-align: center; font-size: 17px; line-height: 20px; }
  .leader .equation .funding { font-size: 20px; }
  .leader .cta { left: 584px; top: 25px; }
</style>
</head>
<body>

<section class="banner sky" aria-label="Skyscraper banner">
  <div class="logo-zone">
    <div class="brand-mark"><span class="dot"></span><span>Fundlark</span></div>
  </div>
  <div class="backdrop" role="img" aria-label="Blue radiating light backdrop"></div>
  <svg class="curve" viewBox="0 0 120 50" preserveAspectRatio="none" aria-hidden="true">
    <path d="M0 0 Q60 42 120 30 L120 50 L0 50 Z" fill="#0a4f9e"/>
    <path d="M0 6 Q60 48 120 36 L120 50 L0 50 Z" fill="#f2f2f2"/>
  </svg>
  <h2 class="headline">
    <span class="big">GET</span>
    <span class="big">YOUR</span>
    <span class="big free">FREE</span>
    <span class="big">GUIDE</span>
    <span class="small first-small">TO</span>
    <span class="small">SUCCESFUL</span>
    <span class="small">CROWD</span>
    <span class="small">FUNDING</span>
  </h2>
  <p class="equation"><span class="word">Project</span><span class="op">+</span><span class="word">Crowd</span><span class="op">=</span><span class="funding">Funding</span></p>
  <svg class="cta" width="86" height="76" viewBox="0 0 86 76" role="img" aria-label="Get started now">
    <defs><linearGradient id="btnSky" x1="0" y1="0" x2="0" y2="1"><stop offset="0" stop-color="#5a5a5a"/><stop offset="1" stop-color="#111"/></linearGradient></defs>
    <path d="M1 1 H85 V60 L43 75 L1 60 Z" fill="url(#btnSky)" stroke="#999" stroke-width="1"/>
    <text x="43" y="22" text-anchor="middle" font-size="16">GET</text>
    <text x="43" y="40" text-anchor="middle" font-size="16">STERTED</text>
    <text x="43" y="58" text-anchor="middle" font-size="16">NOW</text>
  </svg>
</section>

<section class="banner rect" aria-label="Medium rectangle banner">
  <p class="header equation">Project + Crowd <span class="funding">= Funding</span></p>
  <div class="backdrop" role="img" aria-label="Blue radiating light backdrop"></div>
  <svg class="curve" viewBox="0 0 300 100" preserveAspectRatio="none" aria-hidden="true">
    <path d="M0 10 Q120 95 300 68 L300 100 L0 100 Z" fill="#0a4f9e"/>
    <path d="M0 16 Q120 100 300 74 L300 100 L0 100 Z" fill="#f2f2f2"/>
  </svg>
  <div class="brand-mark"><span class="dot"></span><span>Fundlark</span></div>
  <p class="offer">Get Your<br>FREE Guide<br>to Succesful<br>Crowdfunding</p>
  <svg class="cta" width="136" height="38" viewBox="0 0 136 38" role="img" aria-label="Get started now">
    <defs><linearGradient id="btnRect" x1="0" y1="0" x2="0" y2="1"><stop offset="0" stop-color="#5a5a5a"/><stop offset="1" stop-color="#111"/></linearGradient></defs>
    <path d="M1 1 H118 L135 19 L118 37 H1 Z" fill="url(#btnRect)" stroke="#999"/>
    <text x="60" y="24" text-anchor="middle" font-size="13">GET STARTED NOW</text>
  </svg>
</section>

<section class="banner leader" aria-label="Leaderboard banner">
  <div class="backdrop" role="img" aria-label="Blue radiating light backdrop"></div>
  <svg class="curve" viewBox="0 0 80 90" preserveAspectRatio="none" aria-hidden="true">
    <path d="M40 0 Q60 50 0 90 L80 90 L80 0 Z" fill="#0a4f9e"/>
    <path d="M46 0 Q66 50 8 90 L80 90 L80 0 Z" fill="#f2f2f2"/>
  </svg>
  <div class="side">
    <div class="brand-mark"><span class="dot"></span><span>Fundlark</span></div>
  </div>
  <p class="offer">Get Your FREE Guide<br>to Succesful Crowdfunding</p>
  <p class="equation">Project + Crowd <span class="funding">= Funding</span></p>
  <svg class="cta" width="134" height="38" viewBox="0 0 134 38" role="img" aria-label="Get started now">
    <defs><linearGradient id="btnLeader" x1="0" y1="0" x2="0" y2="1"><stop offset="0" stop-color="#5a5a5a"/><stop offset="1" stop-color="#111"/></linearGradient></defs>
    <path d="M1 1 H116 L133 19 L116 37 H1 Z" fill="url(#btnLeader)" stroke="#999"/>
    <text x="60" y="24" text-anchor="middle" font-size="13">GET STARTED NOW</text>
  </svg>
</section>

</body>
</html>
```